Verdal Group Business Card Design

The CEO is looking for a new trendy look for his business card.
You can stay with current branding or come up with something new/creative. It can be 3D, including Medical Office buildings. You can use our logo in a variety of colors. Please include name, title, company name, company website, email address, cell number

Target Market(s)

Real Estate Development and Construction

Industry/Entity Type

Health care real estate

Contact Information for Business Card

Rohesh Kamble, CEO M-702.418.6293 E-roheshkamble@verdal.example Address:4100 Lanyard St, Tampa, FL 33611 www.verdal.example

Other font styles liked:
• Be creative

Requirements
Must have
• Creative, trendy look
Nice to have
• Please go to our website to get a feel- www. verdal.example
Should not have
• small fonts

```html
<!DOCTYPE html>
<html lang="en">
<head>
<meta charset="utf-8">
<title>Verdal Group Business Card</title>
<link href="https://fonts.googleapis.com/css2?family=Poppins:wght@400;500;700;800&display=swap" rel="stylesheet">
<style>
  :root{
    --backdrop:#dfa3a5;
    --navy:#0a1d35;
    --navy-soft:#16233a;
    --red:#e0353b;
    --white:#ffffff;
  }
  *{margin:0;padding:0;box-sizing:border-box}
  html,body{width:1153px;height:1200px;overflow:hidden}
  body{background:var(--backdrop);position:relative;font-family:"Poppins",sans-serif;color:var(--white)}
  .card{position:absolute;left:184px;width:784px;height:448px;border-radius:38px;overflow:hidden;background:var(--navy)}
  .card-front{top:116px}
  .card-back{top:637px}

  .front-band{position:absolute;left:0;top:0;width:100%;height:46px;background:var(--red)}
  .skyline{position:absolute;left:0;right:0;bottom:0;background:linear-gradient(180deg,rgba(22,35,58,0) 0%,var(--navy-soft) 45%,var(--navy-soft) 100%)}
  .front-skyline{height:180px}
  .wordmark{position:absolute;left:0;right:0;top:210px;text-align:center;font-weight:800;font-size:104px;line-height:1;letter-spacing:-4px;color:var(--white)}
  .front-url{position:absolute;left:0;right:0;top:512px;text-align:center;font-size:21px;font-weight:500;letter-spacing:2.5px;top:410px}

  .back-skyline{height:110px}
  .holder-name{position:absolute;left:40px;top:52px;font-weight:700;font-size:51px;line-height:1;letter-spacing:0.5px}
  .holder-title{position:absolute;left:40px;top:115px;width:102px;height:39px;border-radius:9px;background:var(--red);font-size:23px;font-weight:400;letter-spacing:3px;text-align:center;line-height:40px}
  .contact-list{position:absolute;left:48px;top:192px;list-style:none}
  .contact-row{display:flex;align-items:center;height:24px;margin-bottom:23.5px}
  .contact-icon{width:44px;height:22px;border-radius:7px;background:var(--red);display:flex;align-items:center;justify-content:center;margin-right:14px}
  .contact-text{font-size:17px;letter-spacing:1.8px;white-space:nowrap}
  .url-ribbon{position:absolute;left:0;top:354px;width:520px;height:34px}
  .ribbon-text{position:absolute;left:48px;top:354px;height:34px;line-height:36px;font-size:22px;font-weight:500;letter-spacing:2.5px}
  .photo-frame{position:absolute;left:0;top:0;width:784px;height:448px}
</style>
</head>
<body>
  <section class="card card-front">
    <div class="front-band"></div>
    <div class="skyline front-skyline" role="img" aria-label="Faint city skyline silhouette"></div>
    <div class="wordmark">Verdal</div>
    <div class="front-url">www.verdal.example</div>
  </section>

  <section class="card card-back">
    <div class="skyline back-skyline" role="img" aria-label="Faint city skyline silhouette"></div>
    <svg class="photo-frame" viewBox="0 0 784 448" aria-hidden="false">
      <defs>
        <linearGradient id="buildingTones" x1="0" y1="0" x2="0" y2="1">
          <stop offset="0" stop-color="#9fb4d2"/>
          <stop offset="0.4" stop-color="#c9c6bb"/>
          <stop offset="0.7" stop-color="#6f9a86"/>
          <stop offset="1" stop-color="#3d4a3a"/>
        </linearGradient>
      </defs>
      <circle cx="903" cy="558" r="475" fill="var(--white)"/>
      <circle cx="903" cy="558" r="463" fill="url(#buildingTones)" role="img" aria-label="Photograph of a modern medical office building"/>
    </svg>
    <svg class="url-ribbon" viewBox="0 0 520 34" aria-hidden="true">
      <polygon points="0,0 520,0 488,34 0,34" fill="var(--red)"/>
    </svg>

    <h1 class="holder-name">ROHESH KAMBLE</h1>
    <div class="holder-title">CEO</div>

    <ul class="contact-list">
      <li class="contact-row">
        <span class="contact-icon">
          <svg width="16" height="14" viewBox="0 0 16 14"><path d="M8 0 L16 7 H13.5 V14 H9.5 V9.5 H6.5 V14 H2.5 V7 H0 Z" fill="#fff"/></svg>
        </span>
        <span class="contact-text">4100 Lanyard St, Tampa, FL 33611</span>
      </li>
      <li class="contact-row">
        <span class="contact-icon">
          <svg width="14" height="14" viewBox="0 0 24 24"><path d="M6.6 10.8a15 15 0 0 0 6.6 6.6l2.2-2.2c.3-.3.7-.4 1-.2 1.1.4 2.3.6 3.6.6.6 0 1 .4 1 1V20c0 .6-.4 1-1 1C10.6 21 3 13.4 3 4c0-.6.4-1 1-1h3.5c.6 0 1 .4 1 1 0 1.3.2 2.5.6 3.6.1.3 0 .7-.2 1z" fill="#fff"/></svg>
        </span>
        <span class="contact-text">702.418.6293</span>
      </li>
      <li class="contact-row">
        <span class="contact-icon">
          <svg width="20" height="14" viewBox="0 0 20 14"><rect x="0.5" y="0.5" width="19" height="13" fill="#fff"/><path d="M1 1 L10 8 L19 1 M1 13 L7.5 6.5 M19 13 L12.5 6.5" stroke="#e0353b" stroke-width="1.3" fill="none"/></svg>
        </span>
        <span class="contact-text">E-roheshkamble@verdal.example</span>
      </li>
    </ul>

    <div class="ribbon-text">www.verdal.example</div>
  </section>
</body>
</html>
```